Invitation to Celebrate Easter

We need a sign suitable to be affixed to a sandwich board that will serve as an advertisement for our Easter service.

The dimensions of the final product need to be: 2 feet x 3 feet

The text should include:

Join us Easter Sunday
10:15 AM
With Choir, Organ, Brass and Percussion
All are welcome!

I've also uploaded the church logo to be used on the sign.

Target Market(s)

Persons walking by the church on a busy sidewalk in Pelling Square.

Industry/Entity Type

It Service

Font styles to use
Serif
Other font styles liked:
• Goudy Old Style

Colors

Designer to choose colors to be used in the design.

Requirements
Must have
• Colorful and attractive appearance, but tasteful.
Should not have
• NO easter eggs or bunnies! This is for a religious service.

```html
<!DOCTYPE html>
<html lang="en">
<head>
<meta charset="utf-8">
<title>Easter Sunday Service Sign</title>
<link rel="stylesheet" href="https://fonts.googleapis.com/css2?family=Sorts+Mill+Goudy:ital@0;1&family=Cardo:wght@400;700&display=swap">
<style>
  :root {
    --sun-yellow: #f4f53a;
    --light-yellow: #fbfca0;
    --lime: #c9e21f;
    --grass-mid: #8cc31c;
    --grass-deep: #3f7d12;
    --ink: #1f1a14;
    --plum: #8a3a5a;
    --olive-dark: #3e4a12;
    --white: #ffffff;
  }
  * { margin: 0; padding: 0; box-sizing: border-box; }
  html, body {
    width: 877px;
    height: 1200px;
    overflow: hidden;
    background: #f2f2ee;
  }
  .sign {
    position: relative;
    width: 877px;
    height: 1200px;
    overflow: hidden;
    font-family: "Sorts Mill Goudy", "Goudy Old Style", serif;
  }
  .sign__backdrop {
    position: absolute;
    inset: 0;
    background:
      radial-gradient(ellipse 70% 30% at 50% 18%, var(--light-yellow) 0%, rgba(251,252,160,0) 70%),
      linear-gradient(180deg, var(--sun-yellow) 0%, #e8f02c 35%, var(--lime) 55%, var(--grass-mid) 75%, var(--grass-deep) 100%);
  }
  .brand {
    position: absolute;
    top: 172px;
    left: 0;
    width: 100%;
    text-align: center;
    color: var(--ink);
  }
  .brand__name {
    font-size: 38px;
    line-height: 1.1;
    letter-spacing: 0.5px;
  }
  .brand__tagline {
    margin-top: 52px;
    font-size: 14px;
    font-style: italic;
  }
  .headline {
    position: absolute;
    top: 0;
    left: 0;
    width: 100%;
    height: 100%;
    font-weight: 400;
    pointer-events: none;
  }
  .headline span {
    position: absolute;
    line-height: 1;
    white-space: nowrap;
  }
  .headline__join {
    left: 302px;
    top: 380px;
    font-size: 83px;
    color: var(--plum);
  }
  .headline__easter {
    left: 183px;
    top: 401px;
    font-size: 190px;
    background: linear-gradient(90deg, #6e5a10 0%, #8a6414 40%, #9a3a2a 70%, #6a5a18 100%);
    -webkit-background-clip: text;
    background-clip: text;
    color: transparent;
  }
  .headline__sunday {
    left: 352px;
    top: 547px;
    font-size: 128px;
    background: linear-gradient(90deg, var(--olive-dark) 0%, #5a5a14 50%, #7a3a1a 100%);
    -webkit-background-clip: text;
    background-clip: text;
    color: transparent;
  }
  .service {
    position: absolute;
    top: 718px;
    left: 0;
    width: 100%;
    text-align: center;
    font-family: "Cardo", "Goudy Old Style", serif;
    color: var(--ink);
  }
  .service__time {
    font-size: 60px;
    font-weight: 700;
    line-height: 1.1;
  }
  .service__music {
    margin-top: -4px;
    font-size: 40px;
    font-weight: 700;
    line-height: 1.08;
  }
  .welcome {
    position: absolute;
    top: 918px;
    left: 0;
    width: 100%;
    text-align: center;
    font-size: 60px;
    color: var(--white);
    letter-spacing: -0.5px;
  }
</style>
</head>
<body>
  <main class="sign">
    <div class="sign__backdrop" role="img" aria-label="Sunlit spring meadow with fresh green grass blades and soft light glows, a faint cross draped with cloth in the upper right"></div>

    <header class="brand">
      <p class="brand__name">Elmwood Commons Church</p>
      <p class="brand__tagline">A Welcoming Community of Faith and Service</p>
    </header>

    <h1 class="headline">
      <span class="headline__join">Join us</span>
      <span class="headline__easter">Easter</span>
      <span class="headline__sunday">Sunday</span>
    </h1>

    <section class="service">
      <p class="service__time">10:15 AM</p>
      <p class="service__music">With Choir, Organ, Brass<br>and Percussion</p>
    </section>

    <p class="welcome">All are Welcome</p>
  </main>
</body>
</html>
```